Asian Flavours Pre Cooked and Frozen Meals

I would need a one design for frozen food packaging , in plastic pouch, adaptable to 8 different meals:
NEPALI STYLE CHICKEN CURRY
Boneless chicken bites cooked with onions, tomatoes and spices

CHICKEN TIKKA MASALA
Boneless chicken bites stewed with classic spices and cream

CHANA MASALA
Chickpeas in rich masala curry

DAL FRY
Indian style lentils

RED THAI CHICKEN CURRY
Thai style spicy chicken curry

GREEN THAI VEGETARIAN CURRY
Vegetarian Thai style curry

PALAK PANEER
Spinach cream and paneer

VEGETABLE TARKARI
Nepalese style vegetable curry

Target Market(s)

supermarkets

Font styles to use
Sans Serif

Requirements
Must have
• picture of the food, big easy to read text, ingredients and cooking methods in the back , must have a bar code

also a space for
manufacturing date
batch number
net quantity
Nice to have
• all the designs should be the same but different :-)
same font for every product, just the description and picture would change

```html
<!DOCTYPE html>
<html lang="en">
<head>
<meta charset="utf-8">
<title>Sano Bhanchha Foods – Pouch Back</title>
<link href="https://fonts.googleapis.com/css2?family=Open+Sans:wght@400;600;700&display=swap" rel="stylesheet">
<style>
  :root {
    --stage: #1c2a30;
    --rust: #a82b00;
    --rust-pattern: #c03d12;
    --ink: #000000;
    --paper: #ffffff;
    --label-cream: #fdf3d6;
    --field-grey: #dcdcdc;
    --text-dark: #1a1a1a;
  }
  * { margin: 0; padding: 0; box-sizing: border-box; }
  html, body { width: 1200px; height: 675px; overflow: hidden; }
  body {
    background: var(--stage);
    font-family: "Open Sans", sans-serif;
    position: relative;
  }
  .pouch-back {
    position: absolute;
    left: 402px; top: 0;
    width: 396px; height: 675px;
    background: var(--rust);
    overflow: hidden;
  }
  .pouch-art { position: absolute; inset: 0; }
  .tear-label {
    position: absolute;
    left: 166px; top: 58px;
    font-size: 5.4px; font-weight: 700; letter-spacing: .3px;
    color: var(--paper);
    background: var(--rust);
    padding: 0 3px;
  }
  .brand-seal {
    position: absolute;
    left: 141px; top: 113px;
    width: 114px; height: 114px;
    border-radius: 50%;
    background: var(--paper);
    display: flex; align-items: center; justify-content: center;
    text-align: center;
  }
  .brand-name {
    font-size: 15px; font-weight: 700; line-height: 1.1;
    color: var(--text-dark);
  }
  .section-title {
    position: absolute;
    left: 51px;
    font-size: 9.6px; font-weight: 700;
    color: var(--paper);
  }
  .section-body {
    position: absolute;
    left: 51px;
    font-size: 8.6px; font-weight: 600; line-height: 11.4px;
    color: var(--paper);
    text-align: justify;
  }
  .ingredients-title { top: 219px; }
  .ingredients-body { top: 236px; width: 162px; }
  .cooking-title { top: 378px; }
  .cooking-body { top: 398px; width: 306px; }
  .code-label {
    position: absolute;
    left: 37px; top: 541px;
    width: 169px; height: 90px;
    background: var(--label-cream);
    border-radius: 5px;
  }
  .batch-panel {
    position: absolute;
    left: 240px; top: 558px;
    width: 119px; height: 73px;
    background: var(--label-cream);
    border-radius: 4px;
  }
  .batch-row {
    position: absolute; left: 7px;
    font-size: 8px; font-weight: 600;
    color: var(--text-dark);
  }
  .batch-row span { position: absolute; left: 48px; }
  .batch-field {
    position: absolute;
    left: 59px; top: 6px;
    width: 55px; height: 61px;
    background: var(--field-grey);
    border-radius: 3px;
  }
  .net-value {
    position: absolute; left: 74px; top: 53px;
    font-size: 8px; font-weight: 600; color: var(--text-dark);
  }
  .maker-line {
    position: absolute;
    left: 0; width: 396px; top: 651px;
    text-align: center;
    font-size: 8.2px; font-weight: 600;
    color: #1a0800;
  }
  .maker-line b { font-weight: 700; }
</style>
</head>
<body>
  <main class="pouch-back">
    <svg class="pouch-art" width="396" height="675" viewBox="0 0 396 675">
      <rect x="0" y="78" width="396" height="447" fill="var(--ink)"/>
      <g role="img" aria-label="Hand-drawn food and spice doodle pattern in rust tones">
        <path d="M0 78 H396 V178 C375 180 360 160 345 140 C320 110 290 100 250 100 C200 100 160 110 120 102 C80 95 40 90 0 95 Z" fill="var(--rust-pattern)"/>
        <path d="M0 178 C30 185 45 215 40 232 C35 245 15 240 0 245 Z" fill="var(--rust-pattern)"/>
        <path d="M396 238 C375 250 350 265 340 290 C332 310 348 330 396 330 Z" fill="var(--rust-pattern)"/>
        <rect x="0" y="525" width="396" height="150" fill="var(--rust-pattern)"/>
      </g>
      <line x1="0" y1="62.5" x2="396" y2="62.5" stroke="var(--paper)" stroke-width="0.8" stroke-dasharray="4 3"/>
      <g fill="none" stroke="var(--paper)" stroke-width="1">
        <circle cx="243" cy="59" r="2.2"/>
        <circle cx="243" cy="66" r="2.2"/>
        <path d="M245 60 L256 66 M245 65 L256 59"/>
      </g>
    </svg>

    <div class="tear-label">TEAR OR CUT HERE</div>

    <div class="brand-seal">
      <div class="brand-name">Sano<br>Bhanchha<br>Foods</div>
    </div>

    <h2 class="section-title ingredients-title">Ingredients:</h2>
    <p class="section-body ingredients-body">Boneless chicken breast halves - cut into bite-size pieces, small onion chopped, cloves garlic minced, tablespoons curry powder, teaspoon ground cinnamon, teaspoon paprika, bay leaf, teaspoon grated fresh ginger root, teaspoon white sugar, salt to taste skinless, tablespoon tomato paste, 1 cup plain yogurt, cup coconut milk, lemon juice, teaspoon cayenne pepper</p>

    <h2 class="section-title cooking-title">Cooking Instructions:</h2>
    <p class="section-body cooking-body">Lorem Ipsum is simply dummy text of the printing and typesetting industry. Lorem Ipsum has been the industry's standard dummy text ever since the 1500s, when an unknown printer took a galley of type and scrambled it to make a type specimen book. It has survived not only five centuries, but also the leap into electronic typesetting, remaining essentially unchanged. It was popularised in the 1960s with the release of Letraset sheets containing Lorem Ipsum passages, and more recently with desktop publishing software like Aldus PageMaker including versions of Lorem Ipsum.</p>

    <div class="code-label"></div>

    <div class="batch-panel">
      <div class="batch-field"></div>
      <div class="batch-row" style="top:12px">Mfd. date<span>:</span></div>
      <div class="batch-row" style="top:32px">Batch No.<span>:</span></div>
      <div class="batch-row" style="top:52px">Net Qty.<span>:</span></div>
      <div class="net-value">500g</div>
    </div>

    <p class="maker-line">Pkg. Mtri. Mfd. by : <b>Sano Bhanchha Foods</b> (Kiran Marg, Lalitpur, Nepal)</p>
  </main>
</body>
</html>
```